401K Retirement Plan Consultant

Professional & clean lines - not overly busy. We offer two services - 401k administration and HSA administration. Based on the outskirts of Charlotte NC. Communicate the services we offer along with the financial institutions that we work with. Mixture of icons and people pictures.

Current website - tzm401k.com,
It is presently very amateurish.

```html
<!DOCTYPE html>
<html lang="en">
<head>
<meta charset="utf-8">
<title>TZM401k Employee Benefits</title>
<link href="https://fonts.googleapis.com/css2?family=Montserrat:wght@400;500;600;700&display=swap" rel="stylesheet">
<style>
:root{
  --blue:#0a0ae6;
  --ink:#111111;
  --text:#555555;
  --muted:#6b6b6b;
  --white:#ffffff;
  --black:#000000;
  --card-shadow:0 4px 14px rgba(0,0,0,.12);
}
*{margin:0;padding:0;box-sizing:border-box}
html,body{width:1200px;height:4107px;overflow:hidden;background:var(--white)}
body{font-family:'Montserrat',sans-serif;color:var(--ink);position:relative}
.abs{position:absolute}

/* header */
.site-header{position:absolute;left:0;top:0;width:1200px;height:85px;background:var(--white);z-index:3}
.brand{position:absolute;left:108px;top:18px;font-size:40px;font-weight:600;color:var(--ink);letter-spacing:.5px}
.nav{position:absolute;top:32px;display:flex;gap:0}
.nav a{position:absolute;font-size:14px;color:var(--ink);text-decoration:none;white-space:nowrap}
.btn-start{position:absolute;left:912px;top:19px;width:173px;height:48px;background:var(--blue);color:var(--white);font-weight:700;font-size:16px;display:flex;align-items:center;justify-content:center;clip-path:polygon(8% 0,100% 0,92% 100%,0 100%)}

/* hero */
.hero-photo{position:absolute;left:0;top:85px;width:1200px;height:580px;background:linear-gradient(90deg,#3a3f48 0%,#6b6f76 35%,#8a7a6e 60%,#4b4a4e 100%)}
.hero-shade{position:absolute;left:0;top:85px;width:1200px;height:580px;background:rgba(0,0,0,.25)}
.hero-slant{position:absolute;left:0;top:560px;width:1200px;height:110px}
.hero-kicker{position:absolute;left:0;width:1200px;top:258px;text-align:center;color:var(--white);font-weight:700;font-size:27px}
.hero-title{position:absolute;left:0;width:1200px;top:296px;text-align:center;color:var(--white);font-weight:700;font-size:70px;line-height:1}
.btn-contact{position:absolute;left:510px;top:400px;width:175px;height:48px;border:2px solid var(--white);color:var(--white);font-weight:700;font-size:15px;display:flex;align-items:center;justify-content:center;transform:skewX(-14deg)}
.btn-contact span{transform:skewX(14deg)}

/* about */
.about-frame{position:absolute;left:112px;top:776px;width:422px;height:372px;border:4px solid var(--blue)}
.about-photo{position:absolute;left:148px;top:805px;width:415px;height:383px;background:linear-gradient(135deg,#d9d4cc,#8d8a86 55%,#5a5d63)}
.about-title{position:absolute;left:601px;top:790px;font-size:38px;font-weight:600}
.about-copy{position:absolute;left:601px;top:857px;width:430px;font-size:14px;line-height:29px;color:var(--text)}
.pill{position:absolute;left:599px;width:428px;height:51px;border-radius:6px;display:flex;align-items:center;justify-content:center;font-size:15px;font-weight:600;color:var(--blue);background:var(--white);box-shadow:var(--card-shadow)}
.pill.is-active{background:var(--blue);color:var(--white)}
.intro{position:absolute;left:140px;top:1220px;width:920px;text-align:center;font-size:14px;line-height:29px;color:var(--text)}

/* partners */
.section-title{position:absolute;left:0;width:1200px;text-align:center;font-weight:600;color:var(--ink)}
.partner{position:absolute;top:1486px;width:219px;height:92px;background:var(--white);box-shadow:var(--card-shadow);border-radius:3px;display:flex;align-items:center;justify-content:center}
.partner i{display:block;width:120px;height:36px;background:#e4e6ee;border-radius:4px}
.dot{position:absolute;top:1643px;width:13px;height:13px;border-radius:50%;background:#9a9a9a}
.dot.is-active{left:556px;top:1637px;width:24px;height:24px;background:var(--white);border:3px solid var(--blue);box-shadow:0 0 12px rgba(10,10,230,.6)}
.dot.is-active::after{content:"";position:absolute;left:3px;top:3px;width:12px;height:12px;border-radius:50%;background:var(--blue)}

/* services */
.services-band{position:absolute;left:0;top:1730px;width:1200px;height:725px}
.service-card{position:absolute;top:1962px;width:458px;height:319px}
.service-card .photo{position:absolute;inset:0}
.service-label{position:absolute;left:60px;top:247px;width:335px;height:45px;background:var(--blue);color:var(--white);font-weight:700;font-size:16px;display:flex;align-items:center;justify-content:center;clip-path:polygon(9% 0,100% 0,91% 100%,0 100%)}

/* other services */
.feature{position:absolute;width:311px;height:268px;background:var(--white);box-shadow:var(--card-shadow);text-align:center}
.feature .icon{position:absolute;left:112px;top:-46px;width:88px;height:88px;border-radius:50%;background:var(--blue);display:flex;align-items:center;justify-content:center}
.feature h3{position:absolute;left:15px;right:15px;top:56px;font-size:21px;font-weight:500;line-height:33px;color:var(--ink)}
.feature p{position:absolute;left:20px;right:20px;font-size:13px;line-height:28px;color:var(--muted);overflow:hidden}
.feature .tab{position:absolute;left:112px;bottom:0;width:86px;height:7px;background:var(--blue);border-radius:4px 4px 0 0}

/* footer */
.footer-band{position:absolute;left:0;top:3745px;width:1200px;height:362px}
.footer-brand{position:absolute;left:0;width:1200px;top:3890px;text-align:center;color:var(--white);font-size:44px;font-weight:600}
.footer-nav a{position:absolute;top:4008px;color:var(--white);font-size:14px;text-decoration:none}
.footer-rule{position:absolute;left:108px;top:4058px;width:978px;height:1px;background:#cfcfcf}
.copyright{position:absolute;left:0;width:1200px;top:4075px;text-align:center;color:var(--white);font-size:13px}
</style>
</head>
<body>

<header class="site-header">
  <div class="brand">TZM401k</div>
  <nav class="nav">
    <a style="left:515px">HOME</a>
    <a style="left:600px">ABOUT US</a>
    <a style="left:713px">CONTACT US</a>
  </nav>
  <div class="btn-start">Get Started</div>
</header>

<section class="hero">
  <div class="hero-photo" role="img" aria-label="Group of smiling business professionals standing together in a bright office"></div>
  <div class="hero-shade"></div>
  <svg class="hero-slant" viewBox="0 0 1200 110" preserveAspectRatio="none">
    <polygon points="0,85 1200,25 1200,110 0,110" fill="#ffffff"/>
    <polygon points="0,75 1062,32 1062,45 0,98" fill="#0a0ae6"/>
  </svg>
  <div class="hero-kicker">WELCOME TO</div>
  <div class="hero-title">TZM401k</div>
  <div class="btn-contact"><span>Contact Us</span></div>
</section>

<section class="about">
  <div class="about-frame"></div>
  <div class="about-photo" role="img" aria-label="Three colleagues discussing work around a laptop"></div>
  <h2 class="about-title">ABOUT US</h2>
  <p class="about-copy">TZM has been providing employee benefit services since 1987.&nbsp;&nbsp; Our plans gives you the flexibility to customize a retirement plan that meets the specific needs of your company and the employees. Our IRS approved 401(k) plans are:</p>
  <div class="pill is-active" style="top:1017px">Designed especially for smaller plans</div>
  <div class="pill" style="top:1078px">Simple to operate and maintain</div>
  <div class="pill" style="top:1137px">Low-cost recordkeeping and investments</div>
  <p class="intro">Most people realize that, we all have to accept more responsibility for saving for our own retirement.&nbsp; It's widely accepted that Social Security is only meant to provide a modest percentage of your retirement income—so Social Security alone will not be enough.<br>Setting up an employee retirement plan can be a smart way to provide for one of your key assets – your people.<br>Contact us today to request a custom fee comparison or a quote for a startup plan.&nbsp; It's quick and easy.</p>
</section>

<section class="partners">
  <h2 class="section-title" style="top:1408px;font-size:27px">Our Partners</h2>
  <div class="partner" style="left:108px"><i></i></div>
  <div class="partner" style="left:362px"><i></i></div>
  <div class="partner" style="left:614px"><i></i></div>
  <div class="partner" style="left:866px"><i></i></div>
  <span class="dot is-active"></span>
  <span class="dot" style="left:594px"></span>
  <span class="dot" style="left:627px"></span>
</section>

<section class="services">
  <svg class="services-band" viewBox="0 0 1200 725" preserveAspectRatio="none">
    <defs>
      <linearGradient id="bandFill" x1="0" y1="0" x2="1" y2="1">
        <stop offset="0" stop-color="#2a2a2a"/>
        <stop offset=".6" stop-color="#141414"/>
        <stop offset="1" stop-color="#000000"/>
      </linearGradient>
    </defs>
    <polygon points="0,90 1200,20 1200,660 0,725" fill="url(#bandFill)"/>
    <polygon points="0,90 1062,0 1062,18 0,112" fill="#0a0ae6"/>
    <polygon points="0,700 1062,650 1062,662 0,720" fill="#0a0ae6"/>
    <polygon points="0,720 1200,655 1200,725" fill="#ffffff"/>
  </svg>
  <h2 class="section-title" style="top:1868px;font-size:40px;color:#fff">OUR SERVICES</h2>
  <div class="service-card" style="left:123px">
    <div class="photo" role="img" aria-label="Confident businessman in a blue suit in a modern office" style="background:linear-gradient(135deg,#dfe4ea,#9aa5b3 55%,#3d4b63)"></div>
    <div class="service-label">401k administration</div>
  </div>
  <div class="service-card" style="left:615px">
    <div class="photo" role="img" aria-label="Diverse team of professionals standing with arms crossed" style="background:linear-gradient(135deg,#cfd2d6,#8a7d72 50%,#4a4a52)"></div>
    <div class="service-label">HSA administration</div>
  </div>
</section>

<section class="other-services">
  <h2 class="section-title" style="top:2534px;font-size:40px;font-weight:500">OTHER SERVICES</h2>

  <article class="feature" style="left:108px;top:2673px">
    <div class="icon"><svg width="44" height="44" viewBox="0 0 24 24" fill="none" stroke="#fff" stroke-width="1.6"><path d="M7 14a4 4 0 0 1 .5-8 5 5 0 0 1 9.5 1.5A3.3 3.3 0 0 1 17 14z"/><circle cx="12" cy="10" r="2"/><path d="M12 14v4M7 14l-3 5M17 14l3 5"/><circle cx="4" cy="20" r="1.3"/><circle cx="12" cy="19.5" r="1.3"/><circle cx="20" cy="20" r="1.3"/></svg></div>
    <h3>Plan Design &amp; Document Services</h3>
    <p style="top:128px;height:112px">All of our plans are designed using an open architecture investment platform. This allows for a myriad of investment choices for its participants. Instead of</p>
    <span class="tab"></span>
  </article>

  <article class="feature" style="left:440px;top:2673px">
    <div class="icon"><svg width="40" height="40" viewBox="0 0 24 24" fill="none" stroke="#fff" stroke-width="1.6"><rect x="6" y="3" width="12" height="17" rx="1.5"/><path d="M9 8h6M9 11h6M9 14h6M9 17h4"/></svg></div>
    <h3 style="top:60px">IRS 5500 &amp; 1099-R's</h3>
    <p style="top:100px;height:140px">ERISA Form 5500 was created so the government can assess the financial condition, investments, and operations of all employee benefits plans.&nbsp; They are prepared annually along with 1099-R</p>
    <span class="tab"></span>
  </article>

  <article class="feature" style="left:775px;top:2674px">
    <div class="icon"><svg width="46" height="46" viewBox="0 0 24 24" fill="#fff"><circle cx="12" cy="4" r="1.8"/><path d="M12 6.5v3M6 12V10h12v2" stroke="#fff" stroke-width="1.2" fill="none"/><circle cx="6" cy="14.5" r="1.6"/><circle cx="12" cy="14.5" r="1.6"/><circle cx="18" cy="14.5" r="1.6"/><path d="M3.5 20a2.5 2.5 0 0 1 5 0zM9.5 20a2.5 2.5 0 0 1 5 0zM15.5 20a2.5 2.5 0 0 1 5 0z"/></svg></div>
    <h3>Employer Allocation Preparation</h3>
    <p style="top:128px;height:84px">Calculation of Employer Matching and/or Profit Sharing Contribution using various allocation methods.</p>
    <span class="tab"></span>
  </article>

  <article class="feature" style="left:108px;top:3014px">
    <div class="icon"><svg width="40" height="40" viewBox="0 0 24 24" fill="#fff"><ellipse cx="12" cy="5.5" rx="7" ry="2.5"/><path d="M5 8.5c0 1.4 3.1 2.5 7 2.5s7-1.1 7-2.5V11c0 1.4-3.1 2.5-7 2.5S5 12.4 5 11z"/><path d="M5 13.5c0 1.4 3.1 2.5 7 2.5s7-1.1 7-2.5V16c0 1.4-3.1 2.5-7 2.5S5 17.4 5 16z"/></svg></div>
    <h3>Plan Design &amp; Document Services</h3>
    <p style="top:128px;height:112px">Preparation of the Volume Submitter document, adoption agreement and all required forms and notices.&nbsp; These plans are pre-approved by the Internal</p>
    <span class="tab"></span>
  </article>

  <article class="feature" style="left:440px;top:3014px">
    <div class="icon"><svg width="44" height="44" viewBox="0 0 24 24" fill="none" stroke="#fff" stroke-width="1.5"><rect x="11" y="3" width="9" height="7" rx="1"/><path d="M13 5.5h5M13 7.5h3"/><circle cx="8" cy="10" r="2.2" fill="#fff"/><path d="M4 20v-4a4 4 0 0 1 8 0v4z" fill="#fff"/><path d="M3 20h18"/></svg></div>
    <h3 style="top:60px">Employee Education</h3>
    <p style="top:100px;height:140px">TZM401k provides participants with group educational meetings to discuss plan features, investment options, which helps your participants be better prepared for retirement</p>
    <span class="tab"></span>
  </article>

  <article class="feature" style="left:775px;top:3015px">
    <div class="icon"><svg width="44" height="44" viewBox="0 0 24 24" fill="none" stroke="#fff" stroke-width="1.5" stroke-linejoin="round"><path d="M12 3l4 2v4l-4 2-4-2V5z"/><path d="M8 11l4 2v4l-4 2-4-2v-4z"/><path d="M16 11l4 2v4l-4 2-4-2v-4z"/></svg></div>
    <h3>Non-Discrimination Testing</h3>
    <p style="top:128px;height:112px">Nondiscrimination tests ensure that highly compensated employees do not take substantially greater advantage of this tax savings than lower-paid</p>
    <span class="tab"></span>
  </article>

  <article class="feature" style="left:108px;top:3363px">
    <div class="icon"><svg width="44" height="44" viewBox="0 0 24 24" fill="#fff"><circle cx="9" cy="7" r="3.2"/><path d="M3 19a6 6 0 0 1 12 0z"/><circle cx="17" cy="15" r="3" fill="none" stroke="#fff" stroke-width="1.6"/><circle cx="17" cy="15" r="1"/><path d="M17 10.5v1.5M17 18v1.5M12.5 15H14M20 15h1.5" stroke="#fff" stroke-width="1.6"/></svg></div>
    <h3>FSA, HRA and Dependent Care</h3>
    <p style="top:128px;height:112px">Preparation of the Volume Submitter document, adoption agreement and all required forms and notices.&nbsp; These plans are pre-approved by the Internal</p>
    <span class="tab"></span>
  </article>

  <article class="feature" style="left:440px;top:3363px">
    <div class="icon"><svg width="42" height="42" viewBox="0 0 24 24" fill="#fff"><circle cx="10" cy="7" r="3.5"/><path d="M3 20a7 7 0 0 1 11-5.7V20z"/><circle cx="18" cy="17" r="2.6" fill="none" stroke="#fff" stroke-width="1.6"/><path d="M18 12.8v1.4M18 19.8v1.4M13.8 17h1.4M20.8 17h1.4" stroke="#fff" stroke-width="1.6"/></svg></div>
    <h3 style="top:60px">HSA Administration</h3>
    <p style="top:100px;height:140px">An HSA is a unique tax-advantaged account that can be used for paying or reimbursing qualified medical expenses for an individual, spouse or family. To be eligible you must have a</p>
    <span class="tab"></span>
  </article>

  <article class="feature" style="left:775px;top:3364px">
    <div class="icon"><svg width="42" height="42" viewBox="0 0 24 24" fill="#fff"><path d="M12 2l8 3v6c0 5-3.5 9-8 11-4.5-2-8-6-8-11V5z"/><circle cx="12" cy="10" r="2.3" fill="#0a0ae6"/><path d="M8 16a4 4 0 0 1 8 0z" fill="#0a0ae6"/></svg></div>
    <h3 style="top:60px">COBRA Administration</h3>
    <p style="top:100px;height:140px">This is the federal law that provides many workers with the right to continue coverage in a group health plan. This federal law applies to employers with 20 or more employees,</p>
    <span class="tab"></span>
  </article>
</section>

<footer class="site-footer">
  <svg class="footer-band" viewBox="0 0 1200 362" preserveAspectRatio="none">
    <polygon points="0,70 1200,25 1200,362 0,362" fill="#000000"/>
    <polygon points="0,58 1062,0 1062,18 0,82" fill="#0a0ae6"/>
  </svg>
  <div class="footer-brand">TZM401k</div>
  <nav class="footer-nav">
    <a style="left:454px">HOME</a>
    <a style="left:539px">ABOUT US</a>
    <a style="left:652px">CONTACT US</a>
  </nav>
  <div class="footer-rule"></div>
  <div class="copyright">© 2024&nbsp;&nbsp; TZM 401k I All Rights Reserved</div>
</footer>

</body>
</html>
```